Lumen Circle Alliance Slide Deck Template

Design a slide deck template to be used for pitch deck for a company who will be offering services to connect rare disease patients to other patients, pharma/biotech industry in partnership to raise awareness of rare disease, living with a rare disease and treatment choices through on line and in person programs. We need a human element, one that inspires trust and confidence that can be used as a template for our pitch deck etc. We have a logo in progress which will need to have a placeholder for on the slide deck. Thank you

Target Market(s)

Pharma/biotech sector and rare disease patients

Industry/Entity Type

Biotechnology

Font styles to use
Serif
Sans Serif

Colors
63c5b5
00a990
86cfc6
cfeae6
edf8f6
85cae6
0293ce
33a6d7
cee9f5

Requirements
Must have
• Human element. Rare disease aspect if possible. Must inspire trust and confidence.
Nice to have
• Space for our logo which is in development

```html
<!DOCTYPE html>
<html lang="en">
<head>
<meta charset="utf-8">
<title>Lumen Circle Alliance – Slide Deck Template</title>
<link href="https://fonts.googleapis.com/css2?family=Open+Sans:wght@300;400;600;700&family=Merriweather:wght@300;400&display=swap" rel="stylesheet">
<style>
:root{
  --teal:#00a990;--teal2:#63c5b5;--teal3:#86cfc6;--teal4:#cfeae6;--teal5:#edf8f6;
  --blue:#0293ce;--blue2:#33a6d7;--blue3:#85cae6;--blue4:#cee9f5;
  --ink:#5f686d;--grey:#a3abaf;--line:#e3e7e9;--page:#e9ecee;
  --photo-cool:linear-gradient(135deg,#cfe2ec 0%,#f4f8fa 38%,#b9d4e2 62%,#e9f0f3 100%);
  --photo-warm:linear-gradient(120deg,#e6d3c3 0%,#f3ebe3 35%,#cfdde4 70%,#eef3f5 100%);
}
*{box-sizing:border-box;margin:0;padding:0}
html,body{width:899px;height:1200px;overflow:hidden;background:var(--page)}
body{font-family:"Open Sans",Arial,sans-serif;color:var(--ink)}
.deck{display:grid;grid-template-columns:repeat(3,296px);grid-template-rows:repeat(7,168px);gap:3.5px 4px;padding:1.5px 2px}
.slide{position:relative;background:#fff;overflow:hidden;box-shadow:0 1px 2px rgba(0,0,0,.15)}
.abs{position:absolute}
.title{position:absolute;left:13px;top:11px;font-size:9.5px;font-weight:300;color:var(--blue2)}
.logo{position:absolute;right:10px;top:11px;display:flex;align-items:center;gap:2px;font-size:5px;color:var(--teal2)}
.logo i{width:4px;height:4px;border-radius:50%;background:var(--teal2);display:block}
.logo.light{color:#fff}.logo.light i{background:#fff}
.foot{position:absolute;left:0;right:0;bottom:0;height:6px;background:var(--teal);font-size:2.6px;color:#fff;padding:1.6px 0 0 13px}
.foot::after{content:"";position:absolute;right:8px;top:0;width:8px;height:6px;background:var(--teal5)}
.t{font-size:3.3px;line-height:1.35;color:var(--grey)}
.tw{font-size:3.3px;line-height:1.35;color:#fff}
.ph{position:absolute}
.photo-cool{background:var(--photo-cool)}
.photo-warm{background:var(--photo-warm)}
.ico{width:11px;height:11px;border-radius:50%;display:flex;align-items:center;justify-content:center}
.ico svg{width:6px;height:6px}
.hd{font-size:5.8px;color:var(--blue2)}
</style>
</head>
<body>
<main class="deck">

<!-- 1 Text & Bullet -->
<section class="slide">
  <h2 class="title">Text &amp; Bullet Area</h2>
  <div class="logo"><i></i>Lumen Circle Alliance</div>
  <div class="abs" style="left:16px;top:48px;width:80px">
    <p class="hd" style="font-size:4.8px;margin-bottom:9px">Heading Goes Here</p>
    <p class="t" style="margin-bottom:5px">Our programs link people living with rare conditions to peers, care teams and trusted research partners.</p>
    <p class="t" style="margin-bottom:5px">Every session is built around listening, shared stories and clear treatment information.</p>
    <p class="t">Online and in person, members find support when they need it most.</p>
  </div>
  <div class="abs" style="left:108px;top:48px;display:grid;grid-template-columns:92px 86px;row-gap:9px;column-gap:4px">
    <div style="display:flex;gap:4px"><span class="ico" style="background:var(--blue)"><svg viewBox="0 0 10 10"><circle cx="5" cy="5" r="3" fill="none" stroke="#fff"/></svg></span><div><p class="hd">Your Text Here</p><p class="t">Short note about this point goes here.</p></div></div>
    <div style="display:flex;gap:4px"><span class="ico" style="background:var(--teal3)"><svg viewBox="0 0 10 10"><circle cx="5" cy="5" r="3" fill="none" stroke="#fff"/></svg></span><div><p class="hd" style="color:var(--blue3)">Your Text Here</p><p class="t">Short note about this point goes here.</p></div></div>
    <div style="display:flex;gap:4px"><span class="ico" style="background:var(--teal)"><svg viewBox="0 0 10 10"><path d="M2 8V5M5 8V3M8 8V6" stroke="#fff"/></svg></span><div><p class="hd">Your Text Here</p><p class="t">Short note about this point goes here.</p></div></div>
    <div style="display:flex;gap:4px"><span class="ico" style="background:var(--blue3)"><svg viewBox="0 0 10 10"><path d="M2 8L8 2" stroke="#fff"/></svg></span><div><p class="hd" style="color:var(--blue3)">Your Text Here</p><p class="t">Short note about this point goes here.</p></div></div>
    <div style="display:flex;gap:4px"><span class="ico" style="background:var(--blue3)"><svg viewBox="0 0 10 10"><circle cx="5" cy="4" r="2" fill="#fff"/></svg></span><div><p class="hd" style="color:var(--blue3)">Your Text Here</p><p class="t">Short note about this point goes here.</p></div></div>
    <div style="display:flex;gap:4px"><span class="ico" style="background:var(--teal)"><svg viewBox="0 0 10 10"><path d="M2 5l2 2 4-4" stroke="#fff" fill="none"/></svg></span><div><p class="hd">Your Text Here</p><p class="t">Short note about this point goes here.</p></div></div>
    <div style="display:flex;gap:4px"><span class="ico" style="background:var(--teal3)"><svg viewBox="0 0 10 10"><circle cx="5" cy="5" r="3" fill="#fff"/></svg></span><div><p class="hd" style="color:var(--blue3)">Your Text Here</p><p class="t">Short note about this point goes here.</p></div></div>
    <div style="display:flex;gap:4px"><span class="ico" style="background:var(--blue)"><svg viewBox="0 0 10 10"><circle cx="5" cy="5" r="2.5" fill="none" stroke="#fff" stroke-width="1.5"/></svg></span><div><p class="hd">Your Text Here</p><p class="t">Short note about this point goes here.</p></div></div>
  </div>
  <div class="foot">© 2024 Lumen Circle Alliance. All rights reserved.</div>
</section>

<!-- 2 Clients -->
<section class="slide">
  <svg class="abs" style="left:0;top:0" width="296" height="168" viewBox="0 0 296 168" role="img" aria-label="Partner badges">
    <g fill="#7d8a92">
      <rect x="14" y="18" width="40" height="14" rx="2"/>
      <rect x="88" y="14" width="46" height="22" rx="11"/>
      <rect x="160" y="16" width="42" height="18" rx="2"/>
      <rect x="232" y="18" width="44" height="14" rx="7"/>
      <rect x="16" y="68" width="36" height="26" rx="3"/>
      <rect x="244" y="70" width="36" height="22" rx="11"/>
      <circle cx="34" cy="134" r="13"/>
      <circle cx="110" cy="134" r="14"/>
      <rect x="164" y="122" width="40" height="24" rx="3"/>
      <rect x="236" y="124" width="40" height="22" rx="2"/>
    </g>
  </svg>
  <div class="abs" style="left:74px;top:57px;width:144px;height:52px;background:var(--blue2);color:#fff;font-weight:300;font-size:15px;line-height:1.2;text-align:center;padding-top:6px">Our Awesome<br>Client</div>
</section>

<!-- 3 Five columns -->
<section class="slide" style="background:linear-gradient(90deg,var(--teal2),var(--blue2))">
  <div class="abs" style="inset:0;display:grid;grid-template-columns:repeat(5,1fr)">
    <div style="padding:34px 6px 0;border-right:1px solid rgba(255,255,255,.15)"><svg width="20" height="20" viewBox="0 0 20 20" style="display:block;margin:0 auto 20px"><circle cx="10" cy="10" r="8" fill="none" stroke="#fff"/><circle cx="10" cy="10" r="3" fill="none" stroke="#fff"/></svg><p style="font-size:6.5px;color:#fff;margin-bottom:2px">Heading Here</p><p class="tw">Brief description of this service area for patients and partners alike.</p></div>
    <div style="padding:34px 6px 0;background:rgba(255,255,255,.04)"><svg width="20" height="20" viewBox="0 0 20 20" style="display:block;margin:0 auto 20px"><rect x="3" y="3" width="14" height="10" fill="none" stroke="#fff"/><path d="M7 17h6M10 13v4" stroke="#fff"/></svg><p style="font-size:6.5px;color:#fff;margin-bottom:2px">Heading Here</p><p class="tw">Brief description of this service area for patients and partners alike.</p></div>
    <div style="padding:34px 6px 0"><svg width="20" height="20" viewBox="0 0 20 20" style="display:block;margin:0 auto 20px"><circle cx="8" cy="8" r="5" fill="none" stroke="#fff"/><path d="M12 12l5 5" stroke="#fff"/></svg><p style="font-size:6.5px;color:#fff;margin-bottom:2px">Heading Here</p><p class="tw">Brief description of this service area for patients and partners alike.</p></div>
    <div style="padding:34px 6px 0;background:rgba(255,255,255,.04)"><svg width="20" height="20" viewBox="0 0 20 20" style="display:block;margin:0 auto 20px"><rect x="4" y="3" width="12" height="14" fill="none" stroke="#fff"/><circle cx="10" cy="10" r="3" fill="none" stroke="#fff"/></svg><p style="font-size:6.5px;color:#fff;margin-bottom:2px">Heading Here</p><p class="tw">Brief description of this service area for patients and partners alike.</p></div>
    <div style="padding:34px 6px 0"><svg width="20" height="20" viewBox="0 0 20 20" style="display:block;margin:0 auto 20px"><circle cx="10" cy="10" r="8" fill="none" stroke="#fff" stroke-dasharray="3 1.5"/><circle cx="10" cy="10" r="4" fill="none" stroke="#fff"/></svg><p style="font-size:6.5px;color:#fff;margin-bottom:2px">Heading Here</p><p class="tw">Brief description of this service area for patients and partners alike.</p></div>
  </div>
</section>

<!-- 4 Mockup laptop -->
<section class="slide">
  <h2 class="title">Our Mockup Area</h2>
  <div class="logo"><i></i>Lumen Circle Alliance</div>
  <div class="abs" style="left:0;right:0;top:95px;bottom:6px;background:var(--teal2)"></div>
  <div class="ph" role="img" aria-label="Laptop mockup with logo on screen" style="left:60px;top:28px;width:176px;height:100px;background:linear-gradient(#2d3236,#1d2124);border-radius:4px 4px 0 0"></div>
  <div class="abs" style="left:67px;top:34px;width:162px;height:88px;background:#fff;display:flex;align-items:center;justify-content:center;font-size:9px;font-weight:300;color:var(--teal2)">Lumen Circle Alliance</div>
  <div class="abs" style="left:48px;top:128px;width:200px;height:5px;background:#c9ced1;border-radius:0 0 4px 4px"></div>
  <div class="abs tw" style="left:14px;top:56px;width:28px;background:var(--teal);text-align:center;padding:1px">Your Text Goes Here</div>
  <div class="abs tw" style="left:14px;top:78px;width:28px;background:var(--teal3);text-align:center;padding:1px">Your Text Goes Here</div>
  <div class="abs tw" style="left:14px;top:110px;width:28px;background:var(--teal);text-align:center;padding:1px">Your Text Goes Here</div>
  <div class="abs tw" style="left:254px;top:56px;width:28px;background:var(--teal);text-align:center;padding:1px">Your Text Goes Here</div>
  <div class="abs tw" style="left:254px;top:78px;width:28px;background:var(--teal);text-align:center;padding:1px">Your Text Goes Here</div>
  <div class="abs tw" style="left:254px;top:110px;width:28px;background:var(--teal3);text-align:center;padding:1px">Your Text Goes Here</div>
  <div class="foot">© 2024 Lumen Circle Alliance. All rights reserved.</div>
</section>

<!-- 5 Right picture chart -->
<section class="slide">
  <div class="abs" style="left:0;top:0;width:146px;height:168px;background:var(--blue2)">
    <div class="abs" style="left:38px;top:20px;width:70px;height:70px;border-radius:50%;border:1.5px solid #fff;display:flex;align-items:center;justify-content:center;text-align:center;font-size:8.5px;font-weight:300;color:#fff;line-height:1.3">RIGHT<br>PICTURE<br>SLIDE</div>
    <p class="tw abs" style="left:26px;top:112px;width:94px;text-align:center">Connecting patients, families and industry partners to raise awareness and improve everyday life.</p>
  </div>
  <svg class="abs" style="left:160px;top:24px" width="130" height="92" viewBox="0 0 130 92">
    <g fill="var(--blue2)"><rect x="10" y="30" width="5" height="50"/><rect x="38" y="45" width="5" height="35"/><rect x="66" y="38" width="5" height="42"/><rect x="94" y="25" width="5" height="55"/></g>
    <g fill="var(--teal)"><rect x="16" y="52" width="5" height="28"/><rect x="44" y="22" width="5" height="58"/><rect x="72" y="55" width="5" height="25"/><rect x="100" y="18" width="5" height="62"/></g>
    <g fill="var(--blue3)"><rect x="22" y="62" width="5" height="18"/><rect x="50" y="60" width="5" height="20"/><rect x="78" y="48" width="5" height="32"/><rect x="106" y="40" width="5" height="40"/></g>
    <text x="62" y="88" font-size="3" fill="#999">● Sales ● Market ● Cost</text>
  </svg>
  <div class="abs" style="left:158px;top:110px;font-size:16px;font-weight:300;color:var(--blue2)"><span style="font-size:10px">▲</span>85%</div>
  <p class="abs" style="left:162px;top:131px;font-size:4px;color:var(--ink)">Profit</p>
  <p class="t abs" style="left:162px;top:137px;width:46px">Growth in active community members this year.</p>
</section>

<!-- 6 Mockup monitor -->
<section class="slide">
  <div class="abs" style="left:0;top:0;width:296px;height:82px;background:var(--blue2)"></div>
  <h2 class="title" style="color:#fff">Our Mockup Area</h2>
  <p class="abs" style="left:13px;top:36px;font-size:5.5px;color:#fff">Heading Here</p>
  <p class="tw abs" style="left:13px;top:45px;width:100px">We bring patients and partners together through programs built on trust.</p>
  <div class="ph" role="img" aria-label="Desktop monitor mockup with logo on screen" style="left:126px;top:12px;width:160px;height:104px;background:#24292c;border-radius:3px"></div>
  <div class="abs" style="left:130px;top:16px;width:152px;height:90px;background:#fff;display:flex;align-items:center;justify-content:center;font-size:10px;font-weight:300;color:var(--blue2)">Lumen Circle Alliance</div>
  <div class="abs" style="left:196px;top:116px;width:20px;height:14px;background:#c9ced1"></div>
  <div class="abs" style="left:180px;top:130px;width:52px;height:3px;background:#b9bfc2;border-radius:2px"></div>
  <div class="abs" style="left:13px;top:90px;display:flex;gap:5px;width:104px"><span class="ico" style="background:var(--blue2);flex:none;width:8px;height:8px"></span><p class="t">Short supporting line that explains this key message for readers.</p></div>
  <div class="abs" style="left:13px;top:112px;display:flex;gap:5px;width:104px"><span class="ico" style="background:var(--teal);flex:none;width:8px;height:8px"></span><p class="t">Short supporting line that explains this key message for readers.</p></div>
  <div class="foot">© 2024 Lumen Circle Alliance. All rights reserved.</div>
</section>

<!-- 7 Line chart -->
<section class="slide">
  <p class="abs" style="left:22px;top:36px;font-size:11px;font-weight:300;color:var(--teal2);line-height:1.3">This Is Line<br>Chart Slide</p>
  <div class="abs" style="left:22px;top:74px;width:66px;height:8px;background:var(--blue2);font-size:4px;color:#fff;padding:1.5px 0 0 10px">Creative Text Here</div>
  <p class="abs" style="left:22px;top:95px;width:76px;font-size:3.3px;line-height:1.4;color:var(--teal2)">Track engagement across programs and see how community involvement grows over time.</p>
  <svg class="abs" style="left:116px;top:30px" width="170" height="118" viewBox="0 0 170 118" font-size="3" fill="#999">
    <text x="2" y="6">5</text><text x="2" y="24">4</text><text x="2" y="42">3</text><text x="2" y="60">2</text><text x="2" y="78">1</text><text x="2" y="96">0</text>
    <text x="20" y="106">Category 1</text><text x="58" y="106">Category 2</text><text x="96" y="106">Category 3</text><text x="134" y="106">Category 4</text>
    <polyline points="28,28 66,62 104,40 142,26" fill="none" stroke="var(--blue2)" stroke-width="1.3"/>
    <polyline points="28,62 66,22 104,54 142,36" fill="none" stroke="var(--teal)" stroke-width="1.3"/>
  </svg>
</section>

<!-- 8 Title grid -->
<section class="slide">
  <h2 class="title">Your Title Goes Here</h2>
  <div class="logo"><i></i>Lumen Circle Alliance</div>
  <div class="abs" style="left:20px;top:38px;width:256px;height:104px;display:grid;grid-template-columns:repeat(4,1fr);grid-template-rows:1fr 1fr;gap:2px">
    <div class="photo-cool" role="img" aria-label="Photo of care team reviewing a tablet" style="background:linear-gradient(120deg,#3f8fbf 0%,#dbe9f0 40%,#f5f1ec 70%,#9fc6dc 100%)"></div>
    <div style="grid-column:span 2;background:var(--teal);padding:5px"><p style="font-size:7px;color:#fff">Heading Goes Here</p><p class="tw">Short text describing this part of the program.</p></div>
    <div role="img" aria-label="Photo of doctors talking" style="background:linear-gradient(120deg,#f3f6f8 0%,#d3e3ec 45%,#eef2f4 75%,#b6cfdc 100%)"></div>
    <div style="grid-column:span 2;background:var(--blue2);padding:5px"><p style="font-size:7px;color:#fff">Heading Goes Here</p><p class="tw">Short text describing this part of the program.</p></div>
    <div role="img" aria-label="Photo of medical staff group" style="background:linear-gradient(120deg,#e9eff2 0%,#5b9cc4 45%,#f2ede8 70%,#dfe8ed 100%)"></div>
    <div style="background:var(--blue3);padding:5px"><p style="font-size:6px;color:#fff">Heading Goes Here</p><p class="tw">Short text describing this part of the program.</p></div>
  </div>
  <div class="foot">© 2024 Lumen Circle Alliance. All rights reserved.</div>
</section>

<!-- 9 About -->
<section class="slide">
  <div class="ph" role="img" aria-label="Photo of a smiling doctor with a patient" style="inset:0;background:linear-gradient(100deg,#c9d9e3 0%,#f6f7f8 28%,#e9dfd6 48%,#f3f6f7 70%,#d4e2ea 100%)"></div>
  <div class="abs" style="left:146px;top:40px;width:150px;height:94px;background:rgba(51,166,215,.92);padding:12px 10px">
    <p style="font-size:8.5px;font-weight:300;color:#fff;margin-bottom:4px">About Us</p>
    <div style="width:14px;height:1px;background:#fff;margin-bottom:6px"></div>
    <p class="tw" style="margin-bottom:4px">We connect people living with rare diseases to each other and to the partners working on new treatments.</p>
    <p class="tw">Our team listens first, then builds programs that inform and empower.</p>
  </div>
</section>

<!-- 10 Divider -->
<section class="slide">
  <div class="ph" role="img" aria-label="Blue-toned photo of a care team" style="inset:0;background:linear-gradient(120deg,#2f97cf,#5cbbe4 45%,#3aa4d8 70%,#2a8fc7)"></div>
  <div class="logo light" style="font-size:7px;top:14px"><i></i>Lumen Circle Alliance</div>
  <p class="abs" style="left:18px;top:108px;font-size:14.5px;font-weight:700;color:#fff">This Is Your Divider Page</p>
  <p class="abs" style="left:18px;top:128px;font-size:4px;color:#fff">Your Subtitle Goes Here</p>
</section>

<!-- 11 Quote -->
<section class="slide">
  <h2 class="title">Quote Area</h2>
  <div class="logo"><i></i>Lumen Circle Alliance</div>
  <div class="abs" style="left:0;top:34px;width:148px;height:102px;background:var(--blue2);padding:28px 10px 0 14px;color:#fff;font-weight:300;line-height:1.45">
    <p style="font-size:5.6px"><span style="font-size:8px">“</span>Coming together is a beginning. Keeping together is progress. Working together is success.<span style="font-size:8px">”</span></p>
    <p style="margin-top:6px;font-size:5.6px">- Clara Whitfield -</p>
  </div>
  <div class="ph" role="img" aria-label="Photo of a doctor reviewing an X-ray with an older patient" style="left:148px;top:34px;width:148px;height:102px;background:linear-gradient(110deg,#cdd7dd 0%,#efe9e4 35%,#f7f8f9 60%,#b9cfdb 100%)"></div>
  <div class="foot">© 2024 Lumen Circle Alliance. All rights reserved.</div>
</section>

<!-- 12 Brand -->
<section class="slide">
  <h2 class="title">Brand Detailed</h2>
  <div class="logo"><i></i>Lumen Circle Alliance</div>
  <div class="ph photo-warm" role="img" aria-label="Photo of a parent and child at a hospital bed" style="left:20px;top:40px;width:136px;height:104px"></div>
  <div class="abs" style="left:158px;top:40px;width:116px;height:104px;display:grid;grid-template-columns:1fr 1fr;gap:2px;text-align:center">
    <div style="background:var(--blue2);padding:10px 4px"><p style="font-size:4.5px;font-weight:700;color:#fff">System</p><p class="tw">Short text about this area of our work.</p></div>
    <div style="background:var(--teal);padding:10px 4px"><p style="font-size:4.5px;font-weight:700;color:#fff">Technology</p><p class="tw">Short text about this area of our work.</p></div>
    <div style="background:var(--blue3);padding:10px 4px"><p style="font-size:4.5px;font-weight:700;color:#fff">Leisure</p><p class="tw">Short text about this area of our work.</p></div>
    <div style="background:var(--teal3);padding:10px 4px"><p style="font-size:4.5px;font-weight:700;color:#fff">Digital</p><p class="tw">Short text about this area of our work.</p></div>
  </div>
  <div class="foot">© 2024 Lumen Circle Alliance. All rights reserved.</div>
</section>

<!-- 13 Product philosophy -->
<section class="slide">
  <h2 class="title">Product Philosophy</h2>
  <div class="logo"><i></i>Lumen Circle Alliance</div>
  <svg class="abs" style="left:103px;top:42px" width="90" height="90" viewBox="0 0 90 90">
    <g fill="none" stroke-width="14">
      <circle cx="45" cy="45" r="32" stroke="var(--teal)" stroke-dasharray="30.16 201.06" transform="rotate(-90 45 45)"/>
      <circle cx="45" cy="45" r="32" stroke="var(--blue3)" stroke-dasharray="50.27 201.06" transform="rotate(-36 45 45)"/>
      <circle cx="45" cy="45" r="32" stroke="var(--teal2)" stroke-dasharray="40.21 201.06" transform="rotate(54 45 45)"/>
      <circle cx="45" cy="45" r="32" stroke="var(--blue)" stroke-dasharray="80.42 201.06" transform="rotate(126 45 45)"/>
    </g>
    <circle cx="45" cy="45" r="19" fill="#eef3f5"/>
    <circle cx="45" cy="45" r="8" fill="none" stroke="var(--blue)" stroke-width="1"/>
    <g font-size="5" fill="#fff" text-anchor="middle" dominant-baseline="middle">
      <text x="59.5" y="16.5">15%</text><text x="76.6" y="50">25%</text><text x="45" y="77">20%</text><text x="14.6" y="35.1">40%</text>
    </g>
  </svg>
  <div class="abs" style="left:14px;top:48px;width:60px;text-align:right"><p style="font-size:3.8px;color:var(--blue2)">Secure</p><p class="t">Short note on this value.</p></div>
  <span class="ico abs" style="left:78px;top:48px;width:20px;height:20px;background:var(--blue)"></span>
  <div class="abs" style="left:14px;top:104px;width:60px;text-align:right"><p style="font-size:3.8px;color:var(--teal3)">Good Package</p><p class="t">Short note on this value.</p></div>
  <span class="ico abs" style="left:78px;top:104px;width:20px;height:20px;background:var(--teal3)"></span>
  <span class="ico abs" style="left:198px;top:48px;width:20px;height:20px;background:var(--teal)"></span>
  <div class="abs" style="left:222px;top:48px;width:60px"><p style="font-size:3.8px;color:var(--teal)">Well Organized</p><p class="t">Short note on this value.</p></div>
  <span class="ico abs" style="left:198px;top:104px;width:20px;height:20px;background:var(--blue3)"></span>
  <div class="abs" style="left:222px;top:104px;width:60px"><p style="font-size:3.8px;color:var(--blue3)">Publication</p><p class="t">Short note on this value.</p></div>
  <div class="foot">© 2024 Lumen Circle Alliance. All rights reserved.</div>
</section>

<!-- 14 Bar chart -->
<section class="slide">
  <div class="ph" role="img" aria-label="Faded city skyline photo" style="inset:0;background:linear-gradient(#f6f8f9 0%,#e3e9ec 55%,#d6dfe3 100%)"></div>
  <p class="abs" style="left:134px;top:26px;font-size:3px;color:#888">● 2018 ● 2019</p>
  <svg class="abs" style="left:20px;top:30px" width="260" height="108" viewBox="0 0 260 108" font-size="4.5" fill="#fff">
    <rect x="10" y="48" width="14" height="60" fill="var(--blue)"/><rect x="26" y="33" width="14" height="75" fill="var(--blue3)"/>
    <rect x="75" y="63" width="14" height="45" fill="var(--blue)"/><rect x="91" y="18" width="14" height="90" fill="var(--blue3)"/>
    <rect x="140" y="65" width="14" height="43" fill="var(--blue)"/><rect x="156" y="78" width="14" height="30" fill="var(--blue3)"/>
    <rect x="205" y="78" width="14" height="30" fill="var(--blue)"/><rect x="221" y="93" width="14" height="15" fill="var(--blue3)"/>
    <g fill="var(--blue2)"><text x="10" y="45">400</text><text x="26" y="30">500</text><text x="75" y="60">300</text><text x="91" y="15">600</text><text x="140" y="62">290</text><text x="205" y="75">200</text></g>
    <g fill="var(--blue3)"><text x="156" y="75">200</text><text x="221" y="90">100</text></g>
  </svg>
  <div class="abs" style="left:0;right:0;top:138px;bottom:6px;background:var(--teal);display:grid;grid-template-columns:repeat(4,1fr);padding:4px 8px;text-align:center">
    <div><p style="font-size:4px;font-weight:700;color:#fff">Asia</p><p class="tw">Short caption for this region goes here.</p></div>
    <div><p style="font-size:4px;font-weight:700;color:#fff">Africa</p><p class="tw">Short caption for this region goes here.</p></div>
    <div><p style="font-size:4px;font-weight:700;color:#fff">America</p><p class="tw">Short caption for this region goes here.</p></div>
    <div><p style="font-size:4px;font-weight:700;color:#fff">Euro</p><p class="tw">Short caption for this region goes here.</p></div>
  </div>
  <div class="foot" style="background:#0a9a82"></div>
</section>

<!-- 15 World -->
<section class="slide">
  <h2 class="title">Trending In The World</h2>
  <div class="logo"><i></i>Lumen Circle Alliance</div>
  <div class="ph" role="img" aria-label="World map in grey" style="left:12px;top:38px;width:190px;height:112px;border-radius:6px;background:linear-gradient(135deg,#cfd4d7,#b3babe 50%,#d9dddf)"></div>
  <span class="abs" style="left:20px;top:74px;width:20px;height:20px;border-radius:50%;background:var(--blue2);color:#fff;font-size:6px;display:flex;align-items:center;justify-content:center">25%</span>
  <span class="abs" style="left:74px;top:60px;width:26px;height:26px;border-radius:50%;background:var(--teal);color:#fff;font-size:8px;display:flex;align-items:center;justify-content:center">80%</span>
  <span class="abs" style="left:154px;top:68px;width:24px;height:24px;border-radius:50%;background:var(--teal3);color:#fff;font-size:7.5px;display:flex;align-items:center;justify-content:center">75%</span>
  <span class="abs" style="left:132px;top:94px;width:16px;height:16px;border-radius:50%;background:var(--blue3);color:#fff;font-size:5px;display:flex;align-items:center;justify-content:center">15%</span>
  <div class="abs" style="left:206px;top:44px;display:flex;flex-direction:column;gap:10px">
    <div style="display:flex;gap:4px"><span class="ico" style="width:16px;height:16px;border:1px solid var(--blue2);flex:none"></span><div><p style="font-size:3.8px;color:var(--blue2)">Confusion</p><p class="t">Short note on this trend.</p></div></div>
    <div style="display:flex;gap:4px"><span class="ico" style="width:16px;height:16px;border:1px solid var(--teal);flex:none"></span><div><p style="font-size:3.8px;color:var(--teal)">Intangible</p><p class="t">Short note on this trend.</p></div></div>
    <div style="display:flex;gap:4px"><span class="ico" style="width:16px;height:16px;border:1px solid var(--blue3);flex:none"></span><div><p style="font-size:3.8px;color:var(--blue3)">Performance</p><p class="t">Short note on this trend.</p></div></div>
  </div>
  <div class="foot">© 2024 Lumen Circle Alliance. All rights reserved.</div>
</section>

<!-- 16 Vision -->
<section class="slide">
  <h2 class="title">Our Vision &amp; Mission</h2>
  <div class="logo"><i></i>Lumen Circle Alliance</div>
  <div class="abs" style="left:0;right:0;top:34px;height:104px;background:var(--blue2);color:#fff">
    <div class="abs" style="left:14px;top:18px;width:120px">
      <p style="font-size:6.5px;font-weight:300">• Our Vision:</p>
      <p style="font-size:5.5px;font-weight:700;margin:3px 0 6px 4px">Go to the Next Level<br>Without look in the past</p>
      <p class="tw" style="margin-left:4px">Help every person with a rare disease find people, facts and care they can trust.</p>
    </div>
    <div class="abs" style="left:162px;top:18px;width:124px">
      <p style="font-size:6.5px;font-weight:300;margin-bottom:3px">• Our Missions:</p>
      <div style="display:flex;gap:4px;margin-bottom:4px"><span class="ico" style="width:9px;height:9px;background:#fff;flex:none"></span><div><p style="font-size:6px;font-weight:300">Your Text Here</p><p class="tw">Short line describing this mission goal.</p></div></div>
      <div style="display:flex;gap:4px;margin-bottom:4px"><span class="ico" style="width:9px;height:9px;background:#fff;flex:none"></span><div><p style="font-size:6px;font-weight:300">Your Text Here</p><p class="tw">Short line describing this mission goal.</p></div></div>
      <div style="display:flex;gap:4px"><span class="ico" style="width:9px;height:9px;background:#fff;flex:none"></span><div><p style="font-size:6px;font-weight:300">Your Text Here</p><p class="tw">Short line describing this mission goal.</p></div></div>
    </div>
  </div>
  <div class="foot">© 2024 Lumen Circle Alliance. All rights reserved.</div>
</section>

<!-- 17 Services -->
<section class="slide">
  <h2 class="title">Our Services</h2>
  <div class="logo"><i></i>Lumen Circle Alliance</div>
  <div class="ph" role="img" aria-label="Photo of two doctors reviewing a chart" style="left:26px;top:38px;width:100px;height:72px;background:linear-gradient(120deg,#f4f6f7 0%,#d6e3ea 35%,#eee7e0 55%,#bcd3df 80%,#f2f5f6 100%)"></div>
  <p class="abs" style="left:26px;top:114px;font-size:5px;color:var(--blue2)">Your Title Goes Here</p>
  <p class="t abs" style="left:26px;top:121px;width:110px">Short description of how our services support patients and partners every day.</p>
  <div class="abs" style="left:154px;top:40px;display:flex;flex-direction:column;gap:12px;width:130px">
    <div style="display:flex;gap:6px"><span class="ico" style="background:var(--blue);flex:none"></span><div><p style="font-size:5px;color:var(--blue2)">Service Number One</p><p class="t">Short description of this service.</p></div></div>
    <div style="display:flex;gap:6px"><span class="ico" style="background:var(--teal);flex:none"></span><div><p style="font-size:5px;color:var(--teal)">Service Number Two</p><p class="t">Short description of this service.</p></div></div>
    <div style="display:flex;gap:6px"><span class="ico" style="background:var(--blue3);flex:none"></span><div><p style="font-size:5px;color:var(--blue3)">Service Number Three</p><p class="t">Short description of this service.</p></div></div>
  </div>
  <div class="foot">© 2024 Lumen Circle Alliance. All rights reserved.</div>
</section>

<!-- 18 Three columns -->
<section class="slide">
  <h2 class="title">Three Column Description</h2>
  <div class="logo"><i></i>Lumen Circle Alliance</div>
  <p class="abs" style="left:16px;top:40px;width:210px;font-size:5.6px;color:var(--blue2);line-height:1.35">This is place for your header text. Insert your text here, just replace this text with your own text</p>
  <div class="abs" style="left:16px;top:62px;width:266px;display:grid;grid-template-columns:repeat(3,1fr);gap:10px">
    <div><p class="t" style="margin-bottom:4px">Tell patients and partners what matters most about this topic in a few lines.</p><p class="t">Add a second short paragraph here.</p></div>
    <div><p class="t" style="margin-bottom:4px">Tell patients and partners what matters most about this topic in a few lines.</p><p class="t">Add a second short paragraph here.</p></div>
    <div><p class="t" style="margin-bottom:4px">Tell patients and partners what matters most about this topic in a few lines.</p><p class="t">Add a second short paragraph here.</p></div>
  </div>
  <div class="foot">© 2024 Lumen Circle Alliance. All rights reserved.</div>
</section>

<!-- 19 Team -->
<section class="slide">
  <h2 class="title">Our Team</h2>
  <div class="logo"><i></i>Lumen Circle Alliance</div>
  <div class="ph" role="img" aria-label="Portrait photo of team member" style="left:114px;top:30px;width:68px;height:68px;border-radius:50%;background:radial-gradient(circle at 50% 40%,#e3cbb8 0%,#cdb4a2 30%,#9fb2bd 62%,#5f7584 100%)"></div>
  <p class="abs" style="left:0;right:0;top:104px;text-align:center;font-size:3.8px;color:var(--ink)">Mr. Owen Marsh</p>
  <p class="abs" style="left:0;right:0;top:109px;text-align:center;font-size:3.3px;color:var(--teal2)">CEO</p>
  <p class="t abs" style="left:104px;top:115px;width:88px;text-align:center">Short biography of this team member goes here.</p>
  <div class="abs" style="left:140px;top:128px;display:flex;gap:2px"><i style="width:4px;height:4px;border-radius:50%;background:var(--blue)"></i><i style="width:4px;height:4px;border-radius:50%;background:var(--blue)"></i><i style="width:4px;height:4px;border-radius:50%;background:var(--blue)"></i><i style="width:4px;height:4px;border-radius:50%;background:var(--blue)"></i></div>
  <div class="foot">© 2024 Lumen Circle Alliance. All rights reserved.</div>
</section>

<!-- 20 Subscription -->
<section class="slide">
  <h2 class="title">Monthly Subscription</h2>
  <div class="logo"><i></i>Lumen Circle Alliance</div>
  <div class="abs" style="left:0;right:0;top:82px;height:80px;background:var(--blue2)"></div>
  <div class="abs" style="left:42px;top:54px;width:60px;height:84px;background:#fff;box-shadow:0 1px 2px rgba(0,0,0,.15);text-align:center">
    <div style="background:var(--teal3);color:#fff;height:24px;padding-top:3px"><p style="font-size:10px;font-weight:300">$300</p><p style="font-size:2.6px">per month</p></div>
    <div style="font-size:3px;color:#777;line-height:3.6">Single Edition<br>Single Cloud Service<br>1 User<br>Free Update</div>
  </div>
  <div class="abs" style="left:108px;top:50px;width:74px;height:96px;background:#fff;box-shadow:0 1px 2px rgba(0,0,0,.15);text-align:center">
    <div style="background:var(--teal);color:#fff;height:28px;padding-top:4px"><p style="font-size:12px;font-weight:300">$900</p><p style="font-size:2.6px">per month</p></div>
    <div style="font-size:3px;color:#777;line-height:4">Business Edition<br>Single Cloud Service<br>6 User<br>Free Update</div>
  </div>
  <div class="abs" style="left:188px;top:54px;width:60px;height:84px;background:#fff;box-shadow:0 1px 2px rgba(0,0,0,.15);text-align:center">
    <div style="background:var(--blue3);color:#fff;height:24px;padding-top:3px"><p style="font-size:10px;font-weight:300">$400</p><p style="font-size:2.6px">per month</p></div>
    <div style="font-size:3px;color:#777;line-height:3.6">Single Edition<br>Single Cloud Service<br>3 User<br>Free Update</div>
  </div>
</section>

<!-- 21 Table -->
<section class="slide">
  <h2 class="title">Your Title Goes Here</h2>
  <div class="logo"><i></i>Lumen Circle Alliance</div>
  <p class="t abs" style="left:24px;top:36px;width:180px">Short description of the table data goes here.</p>
  <table class="abs" style="left:24px;top:48px;width:250px;border-collapse:collapse;font-size:3px;text-align:center;color:#777">
    <thead><tr style="background:var(--teal);color:#fff;height:6px"><th style="text-align:left;padding-left:4px;font-weight:400">Header</th><th style="font-weight:400">Value</th><th style="font-weight:400">Value</th><th style="font-weight:400">Value</th><th style="font-weight:400">Value</th></tr></thead>
    <tbody style="line-height:8px">
      <tr style="border-bottom:.5px solid var(--line)"><td style="text-align:left;padding-left:4px;color:var(--teal)">Item 1</td><td>10</td><td>15</td><td>16</td><td>18</td></tr>
      <tr style="border-bottom:.5px solid var(--line)"><td style="text-align:left;padding-left:4px;color:var(--teal)">Item 2</td><td>12</td><td>13</td><td>15</td><td>16</td></tr>
      <tr style="border-bottom:.5px solid var(--line)"><td style="text-align:left;padding-left:4px;color:var(--teal)">Item 3</td><td>20</td><td>22</td><td>21</td><td>21</td></tr>
      <tr style="border-bottom:.5px solid var(--line)"><td style="text-align:left;padding-left:4px;color:var(--teal)">Item 4</td><td>10</td><td>21</td><td>12</td><td>11</td></tr>
      <tr style="border-bottom:.5px solid var(--line)"><td style="text-align:left;padding-left:4px;color:var(--teal)">Item 5</td><td>25</td><td>25</td><td>25</td><td>25</td></tr>
      <tr style="border-bottom:.5px solid var(--line)"><td style="text-align:left;padding-left:4px;color:var(--teal)">Item 6</td><td>10</td><td>02</td><td>53</td><td>35</td></tr>
      <tr style="border-bottom:.5px solid var(--line)"><td style="text-align:left;padding-left:4px;color:var(--teal)">Item 7</td><td>35</td><td>35</td><td>65</td><td>32</td></tr>
      <tr style="border-bottom:.5px solid var(--line)"><td style="text-align:left;padding-left:4px;color:var(--teal)">Item 8</td><td>26</td><td>33</td><td>35</td><td>25</td></tr>
      <tr><td style="text-align:left;padding-left:4px;color:var(--teal)">Item 9</td><td>32</td><td>10</td><td>32</td><td>20</td></tr>
    </tbody>
  </table>
  <div class="foot">© 2024 Lumen Circle Alliance. All rights reserved.</div>
</section>

</main>
</body>
</html>
```